"Beyond Marrow Cay" Fictional Book Cover

BEYOND MARROW CAY
By: Dale Pruitt

Here's the intro .

"It had been nearly forty years since Ted Larraby last went to the island from where he was raised. Three months earlier he never would have thought about ever coming back. But life is weird. Things happen quickly and plans change, especially when your very life is at stake. The reason he was going back wasn’t to see old friends...no, no, no. They’re all dead. Of all the kids he grew up with on the island who moved off, he’s the only one still alive. Why?"

Pretty much all just a Lumeno book, by the way.

Target Market(s)

fiction readers

Requirements
Must have
• Somewhat of a dark, mysterious cover is what I'd like to see. Use your imagination. I've never written a fiction book before so I'm very open to ideas

Needs to have my name, DALE PRUITT at the bottom. like my other books, all of which are non-fiction
Nice to have
• Mysterious is what I'm looking for. NOT A HORROR story though. More a guy who left the island years ago, but is being called back to escape the rat race of modern, consumerist culture.

Please remember this NEEDS to jump out as a thumbnail on Bookvale as people are browsing. Mainly the WORDS need to stick out. Lighter words on a say a blue background.

If you want to try to use the attached pic, or something like this, to reflect an island in the cover, that'd be good.

I've also uploaded a couple images I purchased from Pixelcrate, hopefully you can make something work with these.

```html
<!DOCTYPE html>
<html lang="en">
<head>
<meta charset="utf-8">
<title>Beyond Marrow Cay — Cover</title>
<link href="https://fonts.googleapis.com/css2?family=Oranienbaum&family=Pathway+Gothic+One&display=swap" rel="stylesheet">
<style>
  :root {
    --stage: #e6e6e6;
    --sky-light: #dcdfe0;
    --sky-mid: #b9bcbe;
    --water: #8e9193;
    --water-deep: #7d8082;
    --title-light: #f4f4f2;
    --title-dark: #1e1e1e;
    --body-text: #f7f7f5;
    --shade: rgba(0,0,0,0.35);
  }
  * { margin: 0; padding: 0; box-sizing: border-box; }
  html, body { width: 1200px; height: 857px; overflow: hidden; background: var(--stage); }
  .wrap {
    position: absolute; left: 152px; top: 38px;
    width: 896px; height: 780px; display: flex;
    box-shadow: 0 10px 30px rgba(0,0,0,0.18);
  }
  .panel {
    position: relative; height: 780px; overflow: hidden;
    background: linear-gradient(180deg, var(--sky-light) 0%, var(--sky-mid) 40%, var(--water) 75%, var(--water-deep) 100%);
  }
  .back { width: 420px; }
  .spine { width: 56px; border-left: 1px solid rgba(0,0,0,0.12); border-right: 1px solid rgba(0,0,0,0.12);
    background: linear-gradient(180deg, #c9cccd 0%, #9fa2a4 100%); }
  .front { width: 420px; }
  .island-photo { position: absolute; left: 0; width: 100%; }
  .front .island-photo { top: 300px; height: 380px; }
  .back .island-photo { top: 250px; height: 300px; opacity: 0.55; }
  .title {
    position: absolute; left: 0; width: 100%; text-align: center;
    font-family: "Oranienbaum", serif; line-height: 0.95; letter-spacing: 0.5px;
  }
  .title .line-light { display: block; color: var(--title-light); text-shadow: 1px 2px 3px var(--shade); }
  .title .line-dark { display: block; color: var(--title-dark); text-shadow: 1px 1px 2px rgba(255,255,255,0.3); }
  .front .title { top: 96px; font-size: 82px; }
  .back .title { top: 64px; font-size: 46px; }
  .author {
    position: absolute; left: 0; width: 100%; text-align: center;
    font-family: "Oranienbaum", serif; color: var(--title-light);
    text-shadow: 1px 2px 3px var(--shade);
  }
  .front .author { top: 690px; font-size: 46px; }
  .blurb, .bio {
    position: absolute; left: 44px; width: 332px; text-align: center;
    font-family: "Pathway Gothic One", sans-serif; font-size: 15.5px; line-height: 1.32;
    color: var(--body-text); text-shadow: 0 1px 2px var(--shade);
  }
  .blurb { top: 178px; }
  .bio { top: 416px; }
  .bio strong, .blurb strong { font-weight: normal; font-style: italic; font-size: 16.5px; }
  .spine-text {
    position: absolute; left: 0; width: 56px; writing-mode: vertical-rl;
    display: flex; align-items: center; font-family: "Oranienbaum", serif;
  }
  .spine-title { top: 26px; font-size: 30px; }
  .spine-title .light { color: var(--title-light); text-shadow: 1px 1px 2px var(--shade); margin-bottom: 8px; }
  .spine-title .dark { color: var(--title-dark); }
  .spine-author { bottom: 26px; font-size: 28px; color: var(--title-light); text-shadow: 1px 1px 2px var(--shade); }
</style>
</head>
<body>
  <div class="wrap">
    <section class="panel back">
      <svg class="island-photo" viewBox="0 0 420 300" preserveAspectRatio="none" role="img" aria-label="Faded photo of a wooded island shoreline with autumn trees">
        <defs>
          <linearGradient id="backIsle" x1="0" y1="0" x2="0" y2="1">
            <stop offset="0" stop-color="#b9bcbe" stop-opacity="0"/>
            <stop offset="0.35" stop-color="#7d7a58"/>
            <stop offset="0.6" stop-color="#8a6b50"/>
            <stop offset="0.8" stop-color="#8e9193"/>
            <stop offset="1" stop-color="#8e9193" stop-opacity="0"/>
          </linearGradient>
        </defs>
        <rect width="420" height="300" fill="url(#backIsle)"/>
      </svg>
      <h2 class="title"><span class="line-light">BEYOND</span><span class="line-dark">MARROW CAY</span></h2>
      <p class="blurb">"It had been nearly forty years since Ted Larraby last went to the island from where he was raised. Three months earlier he never would have thought about ever coming back. But life is weird. Things happen quickly and plans change, especially when your very life is at stake. The reason he was going back wasn't to see old friends...no, no, no. They're all dead. Of all the kids he grew up with on the island who moved off, he's the only one still alive. <strong>Why?</strong>"</p>
      <p class="bio"><strong>Dale</strong> greatly values spending time with his wife and four children. He has served for many years as a volunteer coach in his children's sports activities. His family is also very active in their church and neighborhood community. Being raised on a small island in Harlow Sound, Maine, Dale is a passionate fan of college and professional hockey and tries to catch a Harborton Gulls game at least once a year with his family.</p>
    </section>

    <section class="panel spine">
      <div class="spine-text spine-title"><span class="light">BEYOND</span><span class="dark">MARROW CAY</span></div>
      <div class="spine-text spine-author">Dale Pruitt</div>
    </section>

    <section class="panel front">
      <svg class="island-photo" viewBox="0 0 420 380" preserveAspectRatio="none" role="img" aria-label="Photo of an island shore with autumn trees, white cottages and a pier above calm grey water with a small buoy">
        <defs>
          <linearGradient id="frontIsle" x1="0" y1="0" x2="0" y2="1">
            <stop offset="0" stop-color="#bcbfc0" stop-opacity="0"/>
            <stop offset="0.12" stop-color="#6f7a56"/>
            <stop offset="0.32" stop-color="#8d6a4a"/>
            <stop offset="0.45" stop-color="#9b9b92"/>
            <stop offset="0.52" stop-color="#7c7d78"/>
            <stop offset="0.6" stop-color="#919496"/>
            <stop offset="1" stop-color="#8a8d8f" stop-opacity="0"/>
          </linearGradient>
        </defs>
        <rect width="420" height="380" fill="url(#frontIsle)"/>
      </svg>
      <h1 class="title"><span class="line-light">BEYOND</span><span class="line-dark">MARROW CAY</span></h1>
      <p class="author">Dale Pruitt</p>
    </section>
  </div>
</body>
</html>
```